Welcome Card Project for bow tie business

We need a welcome message card that will be placed inside a box (packaging) for a mens bow tie business 'Howard Vance'. Howard Vance is a men's brand specializing in unique bow ties of limited editions using quality designer fabrics.
Howard Vance is all about colour, prints and style, where the consumer can add a something a little out of the ordinary and quirky to break out of the mundane 9-5 day.

The dimensions of the double sided welcome card is as follows:
60mm H x 120mm W

One side of the welcome card will have the welcome message with colour and graphics in the background depicting happiness and excitement. It will also include the Chatterly, chirpnet and Snapvue logos and an invitation for customers to share pictures of them wearing the bow ties on Snapvue and chatterly. The website address will also be included here (www.howardvance.example)

The other side of the welcome card will be more conservative with a black on black paisley print design with the 'Howard Vance' logo in a deep purple colour.

Target Market(s)

Men, hipsters, fashionistas, working professionals, women seeking gifts for men

Industry/Entity Type

Conservative

Requirements
Must have
• - Double sided welcome card
- The welcome message (file attached) on one side of the card
- Chatterly + Snapvue logo
- Howard Vance website address (www.howardvance.example)
- Corporate colours: purple, black, orange (on website and in logo) + neutral recycled brown (packaging colour)
- Black on black paisley print on one side of the card
- Howard Vance logo (file attached)- colour: deep purple
Nice to have

Should not have
• - pictures of rainbows

```html
<!DOCTYPE html>
<html lang="en">
<head>
<meta charset="utf-8">
<title>Howard Vance – Welcome Card, Back Side</title>
<link rel="stylesheet" href="https://fonts.googleapis.com/css2?family=Arimo:wght@400;700&family=Dancing+Script:wght@500&display=swap">
<style>
  :root {
    --page: #ffffff;
    --card-black: #0a0a0a;
    --paisley-tone: #161616;
    --brand-purple: #4a1773;
    --accent-orange: #e39a1f;
    --text-light: #ffffff;
    --label-ink: #111111;
  }
  html, body {
    margin: 0;
    padding: 0;
    width: 1200px;
    height: 705px;
    overflow: hidden;
    background: var(--page);
  }
  .canvas {
    position: relative;
    width: 1200px;
    height: 705px;
  }
  .card {
    position: absolute;
    left: 106px;
    top: 102px;
    width: 1004px;
    height: 482px;
    background: var(--card-black);
    overflow: hidden;
  }
  .paisley-print {
    position: absolute;
    inset: 0;
    background: radial-gradient(ellipse at 50% 40%, var(--paisley-tone), var(--card-black) 80%);
  }
  .grid-lines {
    position: absolute;
    inset: 0;
  }
  .brand-name {
    position: absolute;
    left: 360px;
    top: 42px;
    width: 600px;
    text-align: center;
    margin: 0;
    font-family: "Arimo", Arial, sans-serif;
    font-weight: 400;
    font-size: 92px;
    line-height: 1;
    color: var(--brand-purple);
    letter-spacing: 1px;
  }
  .contact {
    position: absolute;
    right: 14px;
    bottom: 12px;
    text-align: right;
    color: var(--text-light);
  }
  .website {
    font-family: "Arimo", Arial, sans-serif;
    font-weight: 700;
    font-size: 13px;
    margin: 0 0 8px 0;
  }
  .share-row {
    display: flex;
    align-items: flex-end;
    gap: 12px;
  }
  .share-invite {
    font-family: "Dancing Script", cursive;
    font-size: 11px;
    letter-spacing: 0.5px;
    margin: 0 0 4px 0;
  }
  .social {
    display: flex;
    align-items: center;
    gap: 5px;
    font-family: "Arimo", Arial, sans-serif;
    font-weight: 700;
    font-size: 12px;
    color: var(--text-light);
  }
  .social-mark {
    width: 10px;
    height: 10px;
    background: var(--text-light);
  }
  .side-label {
    position: absolute;
    left: 0;
    width: 1200px;
    top: 640px;
    margin: 0;
    text-align: center;
    font-family: "Arimo", Arial, sans-serif;
    font-size: 27px;
    color: var(--label-ink);
    letter-spacing: 0.5px;
  }
</style>
</head>
<body>
<main class="canvas">
  <section class="card">
    <div class="paisley-print" role="img" aria-label="Black on black paisley print background"></div>
    <svg class="grid-lines" width="1004" height="482" viewBox="0 0 1004 482" aria-hidden="true">
      <line x1="263" y1="0" x2="263" y2="482" stroke="var(--accent-orange)" stroke-width="6"/>
      <line x1="0" y1="240" x2="1004" y2="236" stroke="var(--accent-orange)" stroke-width="6"/>
    </svg>
    <h1 class="brand-name">Howard Vance</h1>
    <div class="contact">
      <p class="website">www.howardvance.example</p>
      <div class="share-row">
        <p class="share-invite">Share your photos using Howard Vance bow ties</p>
        <span class="social"><span class="social-mark"></span>Chatterly</span>
        <span class="social">Snapvue</span>
      </div>
    </div>
  </section>
  <p class="side-label">BACK SIDE</p>
</main>
</body>
</html>
```